Change an Existing THEME on a Shopify Site

We currently have a Shopify Site that we would like to launch soon. We picked a current theme [Tavel] and have made some basic changes to it but we don't really know what we're doing. We would like a new theme based on this one specifically built for our site. We already brand colours and a logo.

```html
<!DOCTYPE html>
<html lang="en">
<head>
<meta charset="utf-8">
<title>Maple Paws – Pet Store</title>
<link href="https://fonts.googleapis.com/css2?family=Lexend:wght@500;600;700&family=Poppins:wght@400;500;600&display=swap" rel="stylesheet">
<style>
:root{
  --navy:#1b2a5c;
  --teal:#9fd8d3;
  --teal-soft:#dff3f1;
  --teal-icon:#8fcfc9;
  --ink:#1e2233;
  --grey-btn:#5a5a5a;
  --star:#f26b1d;
  --footer:#f0f0f0;
  --white:#ffffff;
}
*{margin:0;padding:0;box-sizing:border-box}
html,body{width:1200px;height:4525px;overflow:hidden}
body{position:relative;background:var(--white);font-family:"Poppins",sans-serif;color:var(--ink)}
.abs{position:absolute}
.heading{font-family:"Lexend",sans-serif;font-weight:600;color:var(--navy);text-transform:uppercase}
.photo{position:absolute}

/* header */
.site-header{position:absolute;left:0;top:0;width:1200px;height:105px;background:var(--white);z-index:3}
.brand-badge{position:absolute;left:72px;top:8px;width:164px;height:164px;border-radius:50%;background:var(--teal);border:6px solid var(--white);box-shadow:0 2px 6px rgba(0,0,0,.15);display:flex;align-items:center;justify-content:center;z-index:4}
.brand-badge span{font-family:"Poppins",sans-serif;font-weight:600;font-size:20px;color:var(--navy)}
.main-nav{position:absolute;top:42px;left:518px;display:flex;gap:20px;font-size:13px;font-weight:500;color:var(--navy)}
.main-nav a{color:var(--ink);text-decoration:none}
.main-nav a.active{color:var(--navy);font-weight:600}
.search{position:absolute;left:875px;top:37px;width:174px;height:31px;border:2px solid var(--navy);border-radius:16px;font-size:12px;color:#aab;padding:6px 14px}

/* hero */
.hero{position:absolute;left:0;top:105px;width:1200px;height:545px;background:var(--teal);overflow:hidden}
.hero h1{position:absolute;left:79px;top:148px;font-size:62px;line-height:62px;font-family:"Lexend",sans-serif;font-weight:600;color:var(--navy)}
.hero p{position:absolute;left:79px;top:287px;width:515px;font-size:14.5px;line-height:24.5px;text-align:justify;color:var(--navy)}
.btn{position:absolute;display:flex;align-items:center;justify-content:center;border-radius:20px;font-size:14px;font-weight:500;text-transform:uppercase}
.btn-navy{background:var(--navy);color:var(--white)}
.hero-photo{left:700px;top:52px;width:490px;height:490px;border-radius:50%;background:radial-gradient(circle at 50% 40%,#e9b57d,#c98a4d 45%,#5f7d3a 80%)}

/* features */
.feature{position:absolute;top:705px;display:flex;align-items:center;gap:14px}
.feature .icon{width:60px;height:60px;border-radius:50%;background:var(--teal-soft);display:flex;align-items:center;justify-content:center}
.feature h4{font-size:14px;font-weight:600;color:var(--navy);text-transform:uppercase}
.feature small{font-size:12px;color:var(--navy)}

/* section titles */
.section-title{position:absolute;left:0;width:1200px;text-align:center}
.section-title .ghost{position:absolute;left:0;width:1200px;top:-26px;font-family:"Lexend",sans-serif;font-weight:500;font-size:76px;color:var(--teal-soft);text-transform:uppercase;letter-spacing:-1px}
.section-title .heading{position:relative;font-size:46px}

/* categories */
.category{position:absolute;top:980px;width:276px;height:274px;overflow:hidden}
.category .photo{left:0;top:0;width:276px;height:220px}
.category .label{position:absolute;left:0;bottom:0;width:276px;height:54px;background:var(--navy);color:var(--white);font-size:22px;display:flex;align-items:center;justify-content:center;text-transform:uppercase}
.arrow{position:absolute;top:1087px;width:60px;height:60px;border-radius:50%;background:var(--teal-soft);display:flex;align-items:center;justify-content:center}

/* products */
.product{position:absolute;width:300px;height:393px;background:var(--white);box-shadow:0 2px 12px rgba(0,0,0,.14)}
.product .photo{left:24px;top:20px;width:262px;height:200px}
.product .name{position:absolute;left:29px;top:236px;width:150px;font-size:13.5px;line-height:20px;text-transform:uppercase;color:var(--ink)}
.product .stars{position:absolute;right:22px;top:240px;font-size:16px;color:var(--star);letter-spacing:1px}
.product .price{position:absolute;left:29px;top:284px;font-size:24px;font-weight:500}
.product .btn{left:26px;top:325px;width:120px;height:40px;border-radius:6px;font-size:12px}
.btn-grey{background:var(--grey-btn);color:var(--white)}
.dots{position:absolute;left:0;width:1200px;display:flex;justify-content:center;gap:4px}
.dots i{width:14px;height:14px;border-radius:50%;border:2px solid var(--navy);display:block}
.dots i.on{background:var(--navy)}

/* about */
.about-title{position:absolute;left:104px;top:2495px}
.about-title .ghost{position:absolute;left:0;top:-20px;font-family:"Lexend",sans-serif;font-weight:500;font-size:74px;color:var(--teal-soft);white-space:nowrap;text-transform:uppercase}
.about-title .heading{position:relative;font-size:46px}
.about-text{position:absolute;left:104px;top:2573px;width:504px;font-size:13px;line-height:26.5px;text-align:justify}

/* sale */
.sale{position:absolute;left:0;top:2975px;width:1200px;height:404px;background:var(--navy)}
.sale .kicker{position:absolute;left:141px;top:93px;font-size:17px;font-weight:600;color:var(--white)}
.sale h2{position:absolute;left:141px;top:120px;font-family:"Lexend",sans-serif;font-weight:600;font-size:46px;color:var(--white)}
.sale p{position:absolute;left:141px;top:180px;width:470px;font-size:13.5px;line-height:24px;color:var(--white)}
.sale-photo{left:650px;top:2922px;width:550px;height:457px;border-radius:48% 48% 0 0;background:radial-gradient(circle at 50% 45%,#f6e7cf,#e4c79e 60%,#c9a774)}

/* testimonials */
.quote-card{position:absolute;top:3613px;width:464px;height:197px;border:2px solid #d8d8d8;border-radius:22px;background:var(--white)}
.quote-mark{position:absolute;top:-44px;left:62px;font-family:"Lexend",sans-serif;font-weight:700;font-size:110px;line-height:110px;color:var(--teal-icon)}
.quote-card h5{position:absolute;left:36px;top:40px;font-size:14px;font-weight:600}
.quote-card .stars{position:absolute;right:34px;top:38px;color:#f2a81d;font-size:16px}
.quote-card p{position:absolute;left:36px;top:68px;width:392px;font-size:12.5px;line-height:21px;font-style:italic;color:#333}
.author{position:absolute;top:3836px;display:flex;align-items:center;gap:14px}
.author .avatar{width:66px;height:66px;border-radius:50%;background:linear-gradient(#d8d2cb,#9c8f84)}
.author b{display:block;font-size:14px;font-weight:600;color:var(--navy);text-transform:uppercase}
.author small{font-size:11px;color:var(--navy)}

/* footer */
.site-footer{position:absolute;left:0;top:4076px;width:1200px;height:449px;background:var(--footer)}
.footer-badge{position:absolute;left:195px;top:106px;width:158px;height:158px;border-radius:50%;background:var(--teal);display:flex;align-items:center;justify-content:center;font-weight:600;font-size:20px;color:var(--navy)}
.social{position:absolute;top:289px;width:30px;height:30px;border-radius:50%;background:var(--navy)}
.footer-col h3{position:absolute;top:100px;font-size:24px;font-weight:500;color:var(--navy);text-transform:uppercase}
.footer-col .rule{position:absolute;top:140px;width:60px;height:2px;background:var(--navy)}
.link{position:absolute;left:511px;font-size:15px;display:flex;align-items:center;gap:14px}
.link::before{content:"";width:10px;height:10px;border-radius:50%;background:var(--navy)}
.contact{position:absolute;left:793px;display:flex;align-items:flex-start;gap:14px;font-size:15px;line-height:25px}
.contact .ic{width:34px;height:34px;border-radius:50%;background:var(--navy);display:flex;align-items:center;justify-content:center;flex:none}
.footer-rule{position:absolute;left:69px;top:380px;width:1064px;height:1px;background:#999}
.copyright{position:absolute;left:69px;top:403px;font-size:14px}
.pay{position:absolute;top:404px;width:30px;height:18px;border-radius:3px}
</style>
</head>
<body>

<header class="site-header">
  <nav class="main-nav">
    <a class="active">HOME</a><a>PRODUCTS</a><a>ABOUT US</a><a>CONTACT US</a>
  </nav>
  <div class="search">Search</div>
  <svg class="abs" style="left:1063px;top:38px" width="30" height="28" viewBox="0 0 30 28"><path d="M2 4h5l4 14h13l3-10H9" fill="none" stroke="#1b2a5c" stroke-width="2.4"/><circle cx="13" cy="23" r="2.4" fill="#1b2a5c"/><circle cx="22" cy="23" r="2.4" fill="#1b2a5c"/><circle cx="25" cy="5" r="5" fill="#1b2a5c"/></svg>
  <svg class="abs" style="left:1107px;top:38px" width="22" height="28" viewBox="0 0 22 28"><circle cx="11" cy="8" r="6.5" fill="#1b2a5c"/><path d="M1 27c0-8 4-12 10-12s10 4 10 12z" fill="#1b2a5c"/></svg>
</header>
<div class="brand-badge"><span>Maple Paws</span></div>

<section class="hero">
  <h1>TAKE CARE OF<br>YOUR LITTLE PETS</h1>
  <p>Lorem ipsum dolor sit amet, consectetur adipiscing elit, sed do eiusmod tempor incididunt ut labore et dolore magna aliqua. Quis ipsum suspendisse ultrices gravida. Risus commodo viverra maecenas accumsan lacus vel facilisis.</p>
  <div class="btn btn-navy" style="left:79px;top:408px;width:136px;height:36px">Shop Now</div>
  <div class="photo hero-photo" role="img" aria-label="Golden puppy with a collar sitting in grass"></div>
</section>

<div class="feature" style="left:79px">
  <div class="icon"><svg width="38" height="26" viewBox="0 0 38 26"><rect x="1" y="3" width="22" height="15" fill="#1b2a5c"/><path d="M23 8h8l5 6v4H23z" fill="#1b2a5c"/><circle cx="8" cy="21" r="3.5" fill="#fff" stroke="#1b2a5c" stroke-width="2"/><circle cx="29" cy="21" r="3.5" fill="#fff" stroke="#1b2a5c" stroke-width="2"/></svg></div>
  <div><h4>Free Shipping</h4><small>Free delivery for all order</small></div>
</div>
<div class="feature" style="left:372px">
  <div class="icon"><svg width="40" height="40" viewBox="0 0 40 40"><circle cx="24" cy="12" r="8" fill="none" stroke="#1b2a5c" stroke-width="3"/><path d="M4 26h8l8 4h10l6-6M4 34h22" fill="none" stroke="#1b2a5c" stroke-width="3"/></svg></div>
  <div><h4>Money Guarantee</h4><small>30 days money back</small></div>
</div>
<div class="feature" style="left:647px">
  <div class="icon"><svg width="44" height="44" viewBox="0 0 44 44"><circle cx="22" cy="22" r="18" fill="none" stroke="#1b2a5c" stroke-width="2.5"/><text x="22" y="26" text-anchor="middle" font-family="Poppins,sans-serif" font-size="11" font-weight="600" fill="#1b2a5c">24/7</text></svg></div>
  <div><h4>24/7 Support</h4><small>Friendly 24/7 suppor</small></div>
</div>
<div class="feature" style="left:900px">
  <div class="icon"><svg width="40" height="36" viewBox="0 0 40 36"><rect x="2" y="8" width="26" height="20" rx="2" fill="#1b2a5c"/><rect x="2" y="13" width="26" height="4" fill="#fff"/><circle cx="30" cy="10" r="8" fill="#1b2a5c" stroke="#fff" stroke-width="2"/><path d="M26 10l3 3 5-6" fill="none" stroke="#fff" stroke-width="2"/></svg></div>
  <div><h4>Secure Payment</h4><small>All cards accepted</small></div>
</div>

<div class="section-title" style="top:886px"><div class="ghost">Product Line-Up</div><div class="heading">Categories</div></div>
<div class="arrow" style="left:70px"><svg width="14" height="20" viewBox="0 0 14 20"><path d="M11 2L3 10l8 8" fill="none" stroke="#fff" stroke-width="2.5"/></svg></div>
<div class="arrow" style="left:1066px"><svg width="14" height="20" viewBox="0 0 14 20"><path d="M3 2l8 8-8 8" fill="none" stroke="#fff" stroke-width="2.5"/></svg></div>
<div class="category" style="left:146px"><div class="photo" role="img" aria-label="Assorted pet toys and chews on a teal surface" style="background:linear-gradient(135deg,#3d8a9a,#74b9c3)"></div><div class="label">Kids and Toys</div></div>
<div class="category" style="left:455px"><div class="photo" role="img" aria-label="Small fluffy dog eating from a bowl" style="background:linear-gradient(135deg,#c8302c,#d89a5a 60%,#e0b27a)"></div><div class="label">Cook and Bake</div></div>
<div class="category" style="left:766px"><div class="photo" role="img" aria-label="Fluffy dog sitting behind a food bowl" style="background:linear-gradient(180deg,#dfe3e6,#d2a06f 70%,#8fbfe0)"></div><div class="label">Lunch and Drink</div></div>

<div class="section-title" style="top:1311px"><div class="ghost">What We Have</div><div class="heading">Our Products</div></div>

<div class="product" style="left:118px;top:1414px"><div class="photo" role="img" aria-label="Dog eating from an automatic feeder" style="background:linear-gradient(135deg,#ece9e6,#c59a5e 60%,#d9d5d0)"></div><div class="name">Crown Bowl<br>Select</div><div class="stars">★★★★★</div><div class="price">€20.00</div><div class="btn btn-navy">Shop Now</div></div>
<div class="product" style="left:450px;top:1414px"><div class="photo" role="img" aria-label="Two small terriers with food bowls" style="background:linear-gradient(135deg,#f1efec,#8c6a48 55%,#c9c5c0)"></div><div class="name">Northern<br>Woods</div><div class="stars">★★★★★</div><div class="price">€20.00</div><div class="btn btn-grey">Add to Cart</div></div>
<div class="product" style="left:782px;top:1414px"><div class="photo" role="img" aria-label="Small dog wearing a jacket on a blue background" style="background:linear-gradient(135deg,#8fc3e6,#5b9fd0 60%,#2a3550)"></div><div class="name">Meadow Mix<br>Boosted</div><div class="stars">★★★★★</div><div class="price">€20.00</div><div class="btn btn-grey">Add to Cart</div></div>
<div class="product" style="left:118px;top:1873px"><div class="photo" role="img" aria-label="Rope toy and leash on a pink background" style="background:linear-gradient(135deg,#f4c6cc,#e9a9b3 60%,#8fb7ad)"></div><div class="name">Pet Food<br>Variable</div><div class="stars">★★★★★</div><div class="price">€20.00</div><div class="btn btn-grey">Shop Now</div></div>
<div class="product" style="left:450px;top:1873px"><div class="photo" role="img" aria-label="Beagle eating from a bowl" style="background:linear-gradient(135deg,#5b4a3f,#b07744 55%,#e7e2dc)"></div><div class="name">Chew Crunch<br>Sticks</div><div class="stars">★★★★★</div><div class="price">€20.00</div><div class="btn btn-grey">Add to Cart</div></div>
<div class="product" style="left:782px;top:1873px"><div class="photo" role="img" aria-label="Two terriers with food bowls" style="background:linear-gradient(135deg,#ebe8e4,#7a6450 55%,#c6c2bd)"></div><div class="name" style="top:246px">Rustic Classic</div><div class="stars">★★★★★</div><div class="price">€20.00</div><div class="btn btn-grey">Add to Cart</div></div>

<div class="dots" style="top:2323px"><i class="on"></i><i></i><i></i><i></i></div>

<div class="about-title"><div class="ghost">Who We Are</div><div class="heading">About Us</div></div>
<p class="about-text">On the other hand, we denounce with righteous indignation and dislike men who are so beguiled and demoralized by the charms of pleasure of the moment, so blinded by desire, that they cannot foresee the pain and trouble that are bound to ensue; and equal blame belongs to those who fail in their duty through weakness of will, which is the same as saying through shrinking from toil and pain. These cases are perfectly simple and easy to distinguish.</p>
<div class="btn btn-navy" style="left:104px;top:2783px;width:122px;height:36px;text-transform:none;font-size:13px">Know More</div>
<div class="photo" role="img" aria-label="Spaniel dog in a field of flowers" style="left:653px;top:2440px;width:436px;height:436px;border-radius:50%;background:radial-gradient(circle at 50% 45%,#e8d8c5,#b06a3a 40%,#7f9a5a 75%,#a99bc0)"></div>

<section class="sale">
  <div class="kicker">AVAILABLE ON STORE</div>
  <h2>SALE OFF UP TO 50%</h2>
  <p>Lorem ipsum dolor sit amet, consectetur adipiscing elit, sed do eiusmod tempor incididunt ut labore et dolore magna aliqua. Quis ipsum suspendisse ultrices gravida.</p>
  <div class="btn" style="left:141px;top:268px;width:147px;height:39px;background:var(--white);color:var(--navy);font-weight:600">Shop Now</div>
</section>
<div class="photo sale-photo" role="img" aria-label="Cream coloured puppy lying down"></div>

<div class="section-title" style="top:3470px"><div class="ghost">What Client Say</div><div class="heading">Testimonials</div></div>

<div class="quote-card" style="left:114px">
  <div class="quote-mark">“</div>
  <h5>Awesome Support...</h5><div class="stars">★★★★★</div>
  <p>"Lorem ipsum dolor sit amet, consectetur adipiscing elit, sed do eiusmod tempor incididunt ut labore et dolore magna aliqua. Quis ipsum suspendisse ultrices gravida. Risus commodo viverra maecenas accumsan lacus vel facilisis."</p>
</div>
<div class="quote-card" style="left:624px">
  <div class="quote-mark">“</div>
  <h5>Great Services....</h5><div class="stars">★★★★★</div>
  <p>"Lorem ipsum dolor sit amet, consectetur adipiscing elit, sed do eiusmod tempor incididunt ut labore et dolore magna aliqua. Quis ipsum suspendisse ultrices gravida. Risus commodo viverra maecenas accumsan lacus vel facilisis."</p>
</div>
<div class="author" style="left:222px"><div class="avatar" role="img" aria-label="Customer portrait"></div><div><b>Owen Reyes</b><small>Lorem ipsum</small></div></div>
<div class="author" style="left:731px"><div class="avatar" role="img" aria-label="Customer portrait"></div><div><b>Liam Carter</b><small>Lorem ipsum</small></div></div>

<div class="dots" style="top:3978px"><i class="on" style="background:var(--teal-icon);border-color:var(--teal-icon)"></i><i style="border-color:var(--teal-icon)"></i><i style="border-color:var(--teal-icon)"></i><i style="border-color:var(--teal-icon)"></i></div>

<footer class="site-footer">
  <div class="footer-badge">Maple Paws</div>
  <div class="social" style="left:222px"></div>
  <div class="social" style="left:259px"></div>
  <div class="social" style="left:296px"></div>

  <div class="footer-col"><h3 style="left:511px">Links</h3><div class="rule" style="left:511px"></div></div>
  <div class="link" style="top:171px">About Us</div>
  <div class="link" style="top:203px">Our Products</div>
  <div class="link" style="top:236px">Contact Us</div>

  <div class="footer-col"><h3 style="left:792px">Contact Us</h3><div class="rule" style="left:792px"></div></div>
  <div class="contact" style="top:170px"><div class="ic"><svg width="14" height="18" viewBox="0 0 14 18"><path d="M7 1a6 6 0 0 1 6 6c0 4-6 10-6 10S1 11 1 7a6 6 0 0 1 6-6z" fill="#fff"/><circle cx="7" cy="7" r="2.2" fill="#1b2a5c"/></svg></div><div>234,Lorem ipsum,<br>Lorem ipsum,Lorem ipsum.</div></div>
  <div class="contact" style="top:236px"><div class="ic"><svg width="16" height="16" viewBox="0 0 16 16"><path d="M3 1l3 3-2 2c1 2 3 4 6 6l2-2 3 3-2 2C7 15 1 9 1 3z" fill="#fff"/></svg></div><div style="padding-top:5px">5550142876</div></div>
  <div class="contact" style="top:287px"><div class="ic"><svg width="16" height="12" viewBox="0 0 16 12"><rect x="0" y="0" width="16" height="12" rx="1" fill="#fff"/><path d="M1 1l7 6 7-6" fill="none" stroke="#1b2a5c" stroke-width="1.5"/></svg></div><div style="padding-top:5px">hello@maplepaws.shop</div></div>

  <div class="footer-rule"></div>
  <div class="copyright">©2016 Maple Paws Supply</div>
  <div class="pay" style="left:977px;background:#c9d3e6"></div>
  <div class="pay" style="left:1011px;background:#e9a253"></div>
  <div class="pay" style="left:1045px;background:#d9dff0"></div>
  <div class="pay" style="left:1079px;background:#6fa9dc"></div>
  <div class="pay" style="left:1103px;background:#e6c38a"></div>
</footer>

</body>
</html>
```